Business Card Design Project 4 Construction Business

I am after a creative, but sleek and simple/ clean business card design. This design will form the basis of future items and might include a logo or simply a creative way to lay out the text of my company name 'kestrel ventures'
I like the simplicity of black and white however I would also be happy to see a splash of colour introduced somehow to give the text some interest and make it stand out.
I would like a double sided card.
I am young (ish!) and professional, offering construction and project management services, what I don't want is the traditional builders type card featuring a cheesy hammer/ saw image etc.
As the company name, kestrel ventures, suggests, we focus on working closely and collaboratively together, in synergy with all stakeholders involved in the projects that we undertake
Construction

```html
<!DOCTYPE html>
<html lang="en">
<head>
<meta charset="utf-8">
<title>Kestrel Ventures – Business Card</title>
<link href="https://fonts.googleapis.com/css2?family=Questrial&family=Didact+Gothic&display=swap" rel="stylesheet">
<style>
  :root {
    --page: #ffffff;
    --card: #302818;
    --tan: #c9ab6e;
    --olive: #6e5d37;
    --accent: #f08a2c;
  }
  html, body {
    margin: 0;
    padding: 0;
    width: 1200px;
    height: 833px;
    overflow: hidden;
    background: var(--page);
  }
  .canvas {
    position: relative;
    width: 1200px;
    height: 833px;
  }
  .card {
    position: absolute;
    left: 377px;
    top: 285px;
    width: 446px;
    height: 264px;
    background: var(--card);
    border-top-right-radius: 60px;
    font-family: "Questrial", "Didact Gothic", sans-serif;
  }
  .card__web {
    position: absolute;
    left: 0;
    top: 0;
  }
  .card__web text {
    font-family: "Didact Gothic", "Questrial", sans-serif;
    font-size: 14px;
    letter-spacing: 0.6px;
    fill: var(--tan);
  }
  .card__brand {
    position: absolute;
    left: 0;
    right: 0;
    top: 68px;
    text-align: center;
    font-size: 15px;
    letter-spacing: 1px;
    color: var(--accent);
    white-space: nowrap;
  }
  .card__phone {
    position: absolute;
    left: 47px;
    top: 128px;
    margin: 0;
    font-size: 32px;
    letter-spacing: 1.2px;
    color: var(--olive);
    white-space: nowrap;
  }
  .card__phone-label {
    margin-right: 22px;
  }
  .card__email {
    position: absolute;
    left: 50px;
    top: 167px;
    margin: 0;
    font-family: "Didact Gothic", "Questrial", sans-serif;
    font-weight: 700;
    font-size: 15.5px;
    letter-spacing: 0.6px;
    color: var(--tan);
    white-space: nowrap;
  }
  .card__address {
    position: absolute;
    left: 0;
    right: 0;
    top: 222px;
    margin: 0;
    text-align: center;
    font-size: 16.5px;
    letter-spacing: 0.3px;
    text-transform: uppercase;
    color: var(--olive);
    white-space: nowrap;
  }
</style>
</head>
<body>
  <div class="canvas">
    <section class="card" aria-label="Kestrel Ventures business card">
      <svg class="card__web" width="446" height="120" viewBox="0 0 446 120" aria-label="www.kestrelventuresgroup.com.au">
        <defs>
          <path id="web-arc" d="M 72 92 Q 222 10 376 92" fill="none"/>
        </defs>
        <text><textPath href="#web-arc" startOffset="50%" text-anchor="middle">www.kestrelventuresgroup.com.au</textPath></text>
      </svg>
      <div class="card__brand">kestrel ventures</div>
      <p class="card__phone"><span class="card__phone-label">Mob.</span>0400 555 019</p>
      <p class="card__email">e.marlow@kestrelventuresgroup.com.au</p>
      <p class="card__address">14 Harbour Ln Kirrawee NSW 2232</p>
    </section>
  </div>
</body>
</html>
```